clearwater mental health web page

this is to be a single page with no links - will function just like an add.
will have 2 biographies
contact info.
Updates

Dear Designers - most of these are too complex.

 Just want one page with contact details (yet to be sorted). No email contact as we can't monitor all emails and if person emails saying suicidal I am potentially accountable if they are successful. Hence- this is just like a listing in a phone book. 
2 photos - one of me the other my husband - with a little blurb next to our names.
No info on fees or appointments etc
I am legally not allowed use language like - "what sets us apart" - it suggests we are better than other clinicians and that is illegal. 
NO EMOTIVE PHOTOS PLEASE! 

Target Market(s)

clients wanting check background and contact information.

Industry/Entity Type

Mental Health

Requirements
Must have
• NEW LOGO
space for photographs
Old web page to complicated
http://lmtq.example.au/index.shtml
Should not have
• anything that flashes.

```html
<!DOCTYPE html>
<html lang="en">
<head>
<meta charset="utf-8">
<title>Clearwater Mental Health</title>
<link rel="stylesheet" href="https://fonts.googleapis.com/css2?family=Cabin:ital,wght@0,400;0,600;0,700;1,400&display=swap">
<style>
:root{
  --sky-top:#5a8ea7;
  --sky-mid:#8fb6bd;
  --sky-low:#c4d8c8;
  --mountain:#34507a;
  --water:#416f87;
  --water-deep:#2d5a73;
  --panel:rgba(22,42,52,0.72);
  --panel-soft:rgba(22,42,52,0.6);
  --text:#ffffff;
  --text-soft:#e4edf0;
  --accent:#7fd3ec;
  --rule:rgba(255,255,255,0.55);
  --logo-ink:#1f4f6b;
}
*{box-sizing:border-box;margin:0;padding:0}
html,body{width:1200px;height:1114px;overflow:hidden}
body{font-family:"Cabin",sans-serif;color:var(--text);letter-spacing:0.05em}
.page{position:relative;width:1200px;height:1114px;overflow:hidden}
.scenery{position:absolute;inset:0;
  background:linear-gradient(180deg,var(--sky-top) 0%,var(--sky-mid) 38%,var(--sky-low) 62%,var(--mountain) 68%,var(--mountain) 72%,var(--water) 77%,var(--water-deep) 100%)}
.brand-rule{position:absolute;top:81px;left:226px;width:748px;height:3px;border-top:1px solid rgba(255,255,255,0.35);border-bottom:1px solid rgba(255,255,255,0.35)}
.brand{position:absolute;top:32px;left:478px;width:242px;height:97px;background:#fff;border-radius:10px;box-shadow:0 3px 8px rgba(0,0,0,0.25);display:flex;align-items:center;gap:12px;padding:0 20px}
.brand-mark{width:30px;height:30px;background:var(--logo-ink);flex:none}
.brand-name{color:var(--logo-ink);font-size:17px;line-height:1.15;letter-spacing:0.06em;text-transform:uppercase}
.panel{position:absolute;background:var(--panel);border-radius:10px}

.profile{top:156px;left:146px;width:908px;height:256px}
.bio{position:absolute;top:16px;width:430px;height:124px}
.bio-1{left:15px}
.bio-2{left:462px}
.portrait{position:absolute;top:0;left:0;width:104px;height:124px;border-radius:8px}
.portrait-1{background:linear-gradient(160deg,#b07a55,#4a5a6a 60%,#d8d8d8)}
.portrait-2{background:linear-gradient(160deg,#8a6a55,#3e4e5e 60%,#b8c0c8)}
.bio-text{position:absolute;top:0;left:122px;right:0;font-size:13px;line-height:21px;color:var(--text-soft)}
.bio-name{display:block;color:var(--accent);font-size:20px;line-height:26px;font-weight:600}
.bio-quals{display:block;font-style:italic;color:#fff}
.profile-rule{position:absolute;top:156px;left:15px;right:15px;border-top:1px dotted var(--rule)}
.contact{position:absolute;top:172px;font-size:13.5px;line-height:23.5px;display:flex;gap:10px}
.contact b{font-weight:700}
.contact svg{flex:none;margin-top:3px}
.c-address{left:20px;width:300px}
.c-phone{left:350px;width:260px}
.c-reg{left:640px;width:250px}

.column{top:430px;width:293px;height:364px;padding:26px 23px}
.col-1{left:146px}
.col-2{left:453px;background:var(--panel-soft)}
.col-3{left:761px}
.col-title{font-size:18px;line-height:22px;font-weight:400;letter-spacing:0.06em;padding-bottom:12px;border-bottom:1px dotted var(--rule);margin-bottom:12px}
.col-2 .col-title{font-size:15px;line-height:22.5px;margin-right:25px}
.focus-list{list-style:none;padding-top:10px}
.focus-list li{display:flex;align-items:center;gap:20px;font-size:16px;margin-bottom:24px}
.thumb{width:61px;height:61px;border-radius:3px}
.thumb-dep{background:linear-gradient(150deg,#2a2030,#5a3a5a)}
.thumb-anx{background:linear-gradient(150deg,#e8d8c8,#a06848)}
.list{list-style:none;font-size:14.5px;line-height:23.5px}
.list li::before{content:"▪";margin-right:7px}
.list .sub{padding-left:6px}
.list .sub::before{content:"o";margin-right:7px}

.services{top:829px;left:146px;width:908px;height:217px;padding:26px 23px}
.services .col-title{margin-bottom:10px}
.service-grid{list-style:none;display:grid;grid-template-columns:230px 315px 260px;font-size:14.5px;line-height:23.5px;padding-left:10px}
.service-grid li::before{content:"▪";margin-right:7px}
.copyright{position:absolute;top:1076px;width:100%;text-align:center;font-size:13px;letter-spacing:0.08em}
</style>
</head>
<body>
<main class="page">
  <div class="scenery" role="img" aria-label="Mountain lake landscape with sky, snow-capped peaks and water"></div>
  <div class="brand-rule"></div>
  <header class="brand">
    <span class="brand-mark"></span>
    <span class="brand-name">Clearwater<br>Mental Health</span>
  </header>

  <section class="panel profile">
    <article class="bio bio-1">
      <div class="portrait portrait-1" role="img" aria-label="Portrait photograph of the first psychologist"></div>
      <div class="bio-text">
        <span class="bio-name">Maren Holloway</span>
        <span class="bio-quals">M. Psych (Clinical), M. Genetic Couns., B.A. (Psych)</span>
        Reg. no: PSY0000481237 Provider no: 3857204L<br>
        Member of the National Psychology Guild
      </div>
    </article>
    <article class="bio bio-2">
      <div class="portrait portrait-2" role="img" aria-label="Portrait photograph of the second psychologist"></div>
      <div class="bio-text">
        <span class="bio-name">Daniel Holloway</span>
        <span class="bio-quals">M. Psych (Clinical), B.Sc. (Psych)</span>
        Reg. no: PSY0000593184 Provider no: 4710366K<br>
        Member of the National Psychology Guild
      </div>
    </article>
    <div class="profile-rule"></div>
    <div class="contact c-address">
      <svg width="18" height="18" viewBox="0 0 18 18"><path d="M9 1 1 9h3v8h10V9h3z" fill="#dde6ea"/></svg>
      <div><b>Address:</b> 24 Fernleigh Place,<br>HALLORAN 6031</div>
    </div>
    <div class="contact c-phone">
      <svg width="18" height="18" viewBox="0 0 18 18"><path d="M4 1c1 0 3 3 3 4s-2 1-1 3 3 4 4 4 1-2 2-1 4 2 4 3-2 3-4 3C8 17 1 9 1 5c0-2 2-4 3-4z" fill="#dde6ea"/></svg>
      <div><b>Phone:</b> (08)9000-4182<br>04-0000-7719</div>
    </div>
    <div class="contact c-reg">
      <div><b>ABN:</b> 41 208 615 937<br><b>ACN:</b> 246093817</div>
    </div>
  </section>

  <section class="panel column col-1">
    <h2 class="col-title">Specialising in the treatment of:</h2>
    <ul class="focus-list">
      <li><span class="thumb thumb-dep" role="img" aria-label="Small photo illustrating depression"></span>Depression</li>
      <li><span class="thumb thumb-anx" role="img" aria-label="Small photo illustrating anxiety"></span>Anxiety</li>
    </ul>
  </section>

  <section class="panel column col-2">
    <h2 class="col-title">Provider of psychological assessment and therapy for other mental healt problems including:</h2>
    <ul class="list">
      <li>Phobias</li>
      <li>Panic</li>
      <li>Adjustment disorder</li>
      <li>Bereavement</li>
      <li>Post-traumatic stress disorder</li>
      <li>Eating disorders</li>
      <li>Obsessive Compulsive disorder</li>
    </ul>
  </section>

  <section class="panel column col-3">
    <h2 class="col-title">Counselling and therapy provided for:</h2>
    <ul class="list">
      <li>Families</li>
      <li>Couples (Couple Care &amp; Relate Program)</li>
      <li>Group</li>
      <li>Individuals</li>
      <li class="sub">Children</li>
      <li class="sub">Adolescents</li>
      <li class="sub">Adults</li>
      <li class="sub">Older persons</li>
    </ul>
  </section>

  <section class="panel services">
    <h2 class="col-title">Other Services:</h2>
    <ul class="service-grid">
      <li>Cognitive Assessment</li>
      <li>Memory &amp; Dementia Screening</li>
      <li>Stress Management</li>
      <li>Neuropsycholog</li>
      <li>Employee Assistance Program</li>
      <li>Medicolegal reports</li>
    </ul>
  </section>

  <footer class="copyright">© Copyright 2013. All rights reserved.</footer>
</main>
</body>
</html>
```